Attractive door board for entrance beautysalon

Make an attractive design for a board that can be glued on the front door of a beauty salon. The salon location has no window in the front so I need something catchy and attractive. The door board contains a list of the services and the website: www.velmora.be, and the text "Enkel op afspraak, bel 0486319542"

Target Market(s)

woman between 16 and 99 years old

Industry/Entity Type

Beauty Salon

Font styles to use
Sans Serif

Requirements
Must have
• A very nice, attractive but sober design.
• It must have a classy Marvaux, Quen, ... chique design.
• The logo must be on it (in attachment)
• There must be the following list in it:
• Gelaatsverzorging
• Wimperverlenging
• Wimperlifting
• Suikerontharing
• Permanente Make Up
• Airbrush Tanning
• Manicure - Pedicure - Tovira
• and then the website www.velmora.be, and the text "Enkel op afspraak, bel 0486319542"
Nice to have
• a catchy design,
• max. width can be 75 cm and max height 180 cm as it is a design for a board that will be glued on a door.
Should not have
• orchid flowers, buddha look a likes

```html
<!DOCTYPE html>
<html lang="nl">
<head>
<meta charset="utf-8">
<title>Velmora – Schoonheidsinstituut deurbord</title>
<link href="https://fonts.googleapis.com/css2?family=Montserrat:wght@300;400&display=swap" rel="stylesheet">
<style>
  :root {
    --board-tan: #d7a588;
    --ink-white: #ffffff;
    --rule: rgba(255, 255, 255, 0.55);
    --skin-warm: #e2b59c;
    --skin-light: #f1d5c4;
    --studio-white: #ffffff;
  }
  html, body {
    margin: 0;
    padding: 0;
    width: 1200px;
    height: 2880px;
    overflow: hidden;
    background: var(--board-tan);
  }
  .door-board {
    position: relative;
    width: 1200px;
    height: 2880px;
    background: var(--board-tan);
    color: var(--ink-white);
    font-family: "Montserrat", sans-serif;
    font-weight: 300;
  }
  .hero-portrait {
    position: absolute;
    left: 166px;
    top: 213px;
    width: 855px;
    height: 934px;
    background: linear-gradient(90deg, var(--skin-warm) 0%, var(--skin-light) 45%, #f7e6dc 66%, var(--studio-white) 74%, var(--studio-white) 100%);
  }
  .brand-mark {
    position: absolute;
    left: 480px;
    top: 1228px;
    width: 236px;
    height: 236px;
    border: 2px solid var(--ink-white);
    border-radius: 50%;
    display: flex;
    align-items: center;
    justify-content: center;
    box-sizing: border-box;
  }
  .brand-mark__name {
    font-size: 24px;
    font-weight: 300;
    letter-spacing: 0.3em;
    padding-left: 0.3em;
    line-height: 1;
  }
  .centered {
    position: absolute;
    left: 0;
    right: 0;
    text-align: center;
    margin: 0;
  }
  .brand-name {
    top: 1560px;
    font-size: 64px;
    font-weight: 300;
    letter-spacing: 0.85em;
    padding-left: 0.85em;
    line-height: 1;
  }
  .brand-tagline {
    top: 1670px;
    font-size: 21px;
    font-weight: 400;
    letter-spacing: 1.05em;
    padding-left: 1.05em;
    line-height: 1;
  }
  .divider {
    position: absolute;
    left: 142px;
    width: 914px;
    height: 2px;
    background: var(--rule);
  }
  .divider--upper { top: 1789px; }
  .divider--lower { top: 2121px; }
  .contact-block {
    top: 1904px;
    font-size: 35px;
    letter-spacing: 0.16em;
    line-height: 43px;
    font-weight: 400;
  }
  .service-list {
    top: 2206px;
    list-style: none;
    padding: 0;
    font-size: 34px;
    letter-spacing: 0.16em;
    line-height: 41.5px;
    font-weight: 400;
  }
  .service-list li { margin: 0; }
</style>
</head>
<body>
  <main class="door-board">
    <div class="hero-portrait" role="img" aria-label="Portretfoto van een vrouw met verzorgde huid tegen een witte achtergrond"></div>

    <div class="brand-mark" role="img" aria-label="Logo Velmora">
      <span class="brand-mark__name">VELMORA</span>
    </div>

    <h1 class="centered brand-name">VELMORA</h1>
    <p class="centered brand-tagline">SCHOONHEIDSINSTITUUT</p>

    <div class="divider divider--upper"></div>

    <p class="centered contact-block">
      WWW.VELMORA.BE<br>
      ENKEL OP AFSPRAAK, BEL 0486319542
    </p>

    <div class="divider divider--lower"></div>

    <ul class="centered service-list">
      <li>GELAATSVERZORGING</li>
      <li>WIMPERVERLENGING</li>
      <li>WIMPERLIFTING</li>
      <li>SUIKERONTHARING</li>
      <li>PERMANENTE MAKE UP</li>
      <li>AIRBRUSH TANNING</li>
      <li>MANICURE - PEDICURE - TOVIRA</li>
    </ul>
  </main>
</body>
</html>
```